Vell Motorsport Pty. Limited
Business Stationary
Vell Motorsport Pty. Limited -
Creative Brief
Professional
Dorin Keplow
Managing Director
P.O. Box 742 Larkfield NSW 2999 AUSTRALIA
vellmotorsport@mailvex.co.uk
www.vellmotorsport-example.com.au

```html
<!DOCTYPE html>
<html lang="en">
<head>
<meta charset="utf-8">
<title>Vell Motorsport – Business Card</title>
<link rel="stylesheet" href="https://fonts.googleapis.com/css2?family=Arimo:wght@400;700&family=Tinos&display=swap">
<style>
  :root {
    --stage: #f4f4f4;
    --stage-low: #e4e4e4;
    --label: #7a7a7a;
    --orange: #f38a1d;
    --orange-light: #f9a341;
    --ink-soft: #8c8c8c;
    --black: #0d0d0d;
    --black-edge: #262626;
    --white: #ffffff;
  }
  * { margin: 0; padding: 0; box-sizing: border-box; }
  html, body { width: 1200px; height: 379px; overflow: hidden; }
  body {
    background: linear-gradient(to bottom, var(--stage) 0%, var(--stage) 65%, var(--stage-low) 100%);
    font-family: "Arimo", Arial, sans-serif;
    position: relative;
  }
  .side-label {
    position: absolute;
    top: 62px;
    width: 338px;
    text-align: center;
    font-family: "Tinos", "Times New Roman", serif;
    font-size: 26px;
    letter-spacing: 1px;
    color: var(--label);
  }
  .card {
    position: absolute;
    top: 96px;
    width: 338px;
    height: 228px;
    overflow: hidden;
    box-shadow: 0 10px 12px -8px rgba(0,0,0,0.35);
  }
  .card--front { left: 84px; background: var(--white); border: 1px solid #e2e2e2; }
  .card--back-dark { left: 434px; background: radial-gradient(ellipse at 50% 45%, var(--black-edge) 0%, var(--black) 70%); }
  .card--back-orange { left: 775px; background: radial-gradient(ellipse at 50% 55%, var(--orange-light) 0%, var(--orange) 75%); }

  .brand {
    position: absolute;
    display: flex;
    align-items: center;
    gap: 6px;
    font-weight: 700;
    white-space: nowrap;
  }
  .brand__dot { width: 8px; height: 8px; border-radius: 50%; background: currentColor; }
  .card--front .brand { left: 22px; top: 58px; font-size: 19px; color: var(--orange); }
  .card--back-dark .brand,
  .card--back-orange .brand {
    left: 50%; top: 46%; transform: translate(-50%, -50%);
    font-size: 16px;
  }
  .card--back-dark .brand { color: var(--orange); }
  .card--back-orange .brand { color: var(--white); }

  .contact {
    position: absolute;
    left: 22px;
    top: 146px;
    font-size: 7px;
    line-height: 10px;
    color: var(--ink-soft);
  }
  .contact__web { color: var(--orange); }
  .person {
    position: absolute;
    left: 202px;
    top: 148px;
  }
  .person__name { font-size: 10px; color: var(--orange); }
  .person__role { font-size: 7px; color: var(--ink-soft); margin-top: 3px; }
</style>
</head>
<body>
  <div class="side-label" style="left:84px">FRONT</div>
  <div class="side-label" style="left:434px">BACK</div>
  <div class="side-label" style="left:775px">BACK</div>

  <section class="card card--front" aria-label="Card front">
    <div class="brand"><span class="brand__dot"></span>VellMotorsport</div>
    <div class="contact">
      <p>P.O. Box 742 Larkfield</p>
      <p>NSW 2999 AUSTRALIA</p>
      <p>T: 0412 000 000 &nbsp; F: 02 9000 0000</p>
      <p>E: vellmotorsport@mailvex.co.uk</p>
      <p class="contact__web">www.vellmotorsport-example.com.au</p>
    </div>
    <div class="person">
      <p class="person__name">Dorin Keplow</p>
      <p class="person__role">Managing Director</p>
    </div>
  </section>

  <section class="card card--back-dark" aria-label="Card back, dark">
    <div class="brand"><span class="brand__dot"></span>VellMotorsport</div>
  </section>

  <section class="card card--back-orange" aria-label="Card back, orange">
    <div class="brand"><span class="brand__dot"></span>VellMotorsport</div>
  </section>
</body>
</html>
```